Business Card Design Project

We consult with hotels on setting rates and maximizing a revenue strategy

Industry/Entity Type

Business

Contact Information for Business Card

I am not sure what I want. Our company offers high level consulting to hotels around the country but we are also laid back. I would like something that is professional but also shows the laid back side

```html
<!DOCTYPE html>
<html lang="en">
<head>
<meta charset="utf-8">
<title>Harborline Business Card</title>
<link href="https://fonts.googleapis.com/css2?family=Open+Sans:wght@400;600;700&display=swap" rel="stylesheet">
<style>
  :root{
    --backdrop:#d4d4d4;
    --paper:#ffffff;
    --band-grey:#7d8b8f;
    --teal:#1b7770;
    --teal-light:#5f9c96;
    --slate:#8a9a9c;
    --navy:#252c39;
    --brown:#3b2a22;
    --ink:#333333;
  }
  *{margin:0;padding:0;box-sizing:border-box}
  html,body{width:1200px;height:901px;overflow:hidden}
  body{background:var(--backdrop);font-family:"Open Sans",Arial,sans-serif;position:relative}
  .card{position:absolute;width:540px;height:309px;background:var(--paper);
        box-shadow:0 6px 18px rgba(0,0,0,.18);overflow:hidden}
  .card--front{left:80px;top:90px}
  .card--back{left:580px;top:490px}
  .card svg.shapes{position:absolute;inset:0;width:100%;height:100%}
  .brand{position:absolute;display:flex;align-items:center;gap:10px}
  .brand__mark{width:16px;height:16px;background:var(--teal)}
  .brand__name{font-weight:700;color:var(--brown);letter-spacing:1px}
  .card--front .brand{left:150px;top:120px}
  .card--front .brand__name{font-size:34px}
  .card--back .brand{left:300px;top:58px}
  .card--back .brand__name{font-size:24px}
  .site{position:absolute;right:28px;bottom:18px;display:flex;align-items:center;gap:8px;
        color:#fff;font-size:13px}
  .person{position:absolute;left:34px;top:54px}
  .person__name{font-size:21px;color:var(--ink);font-weight:400}
  .person__name b{color:var(--teal);font-weight:700}
  .person__role{font-size:14px;color:var(--ink)}
  .contacts{position:absolute;left:34px;top:122px;list-style:none}
  .contacts li{display:flex;align-items:center;gap:12px;margin-bottom:10px;font-size:14px;color:var(--ink);line-height:1.15}
  .icon{width:26px;height:26px;background:var(--teal);display:flex;align-items:center;justify-content:center;flex:none}
</style>
</head>
<body>

<section class="card card--front" aria-label="Card front">
  <svg class="shapes" viewBox="0 0 540 309" preserveAspectRatio="none">
    <rect x="0" y="0" width="540" height="18" fill="var(--band-grey)"/>
    <polygon points="0,160 0,309 540,309 540,240 300,230" fill="var(--slate)"/>
    <polygon points="0,170 0,309 540,309 540,255 250,235" fill="var(--teal)"/>
    <polygon points="0,190 0,309 540,309 540,268 230,240" fill="var(--teal-light)"/>
    <polygon points="0,185 40,170 0,309" fill="var(--navy)"/>
    <polygon points="210,235 540,270 540,309 230,309" fill="var(--navy)"/>
  </svg>
  <div class="brand"><span class="brand__mark"></span><span class="brand__name">HARBORLINE</span></div>
  <div class="site">
    <svg width="16" height="16" viewBox="0 0 16 16" fill="none" stroke="#fff" stroke-width="1.2">
      <circle cx="8" cy="8" r="6.5"/><ellipse cx="8" cy="8" rx="3" ry="6.5"/><line x1="1.5" y1="8" x2="14.5" y2="8"/>
    </svg>
    <span>www.HarborlineRMS.com</span>
  </div>
</section>

<section class="card card--back" aria-label="Card back">
  <svg class="shapes" viewBox="0 0 540 309" preserveAspectRatio="none">
    <rect x="0" y="0" width="540" height="22" fill="var(--band-grey)"/>
    <polygon points="540,150 540,309 260,309 200,290" fill="var(--slate)"/>
    <polygon points="540,165 540,309 260,309 200,292" fill="var(--teal)"/>
    <polygon points="540,190 540,309 300,309 210,290" fill="var(--teal-light)"/>
    <polygon points="540,210 540,309 260,309 200,292" fill="var(--navy)"/>
    <polygon points="0,262 200,290 260,309 0,309" fill="var(--teal)"/>
    <polygon points="0,275 150,300 160,309 0,309" fill="var(--slate)"/>
    <polygon points="0,282 30,309 0,309" fill="var(--navy)"/>
  </svg>
  <div class="brand"><span class="brand__mark"></span><span class="brand__name">HARBORLINE</span></div>
  <div class="person">
    <p class="person__name"><b>DANA</b> WHITFIELD</p>
    <p class="person__role">Regional Revenue Manager</p>
  </div>
  <ul class="contacts">
    <li><span class="icon"><svg width="14" height="14" viewBox="0 0 24 24" fill="#fff"><path d="M6.6 10.8a15 15 0 0 0 6.6 6.6l2.2-2.2a1 1 0 0 1 1-.25 11.4 11.4 0 0 0 3.6.57 1 1 0 0 1 1 1V20a1 1 0 0 1-1 1A17 17 0 0 1 3 4a1 1 0 0 1 1-1h3.5a1 1 0 0 1 1 1c0 1.25.2 2.45.57 3.57a1 1 0 0 1-.25 1z"/></svg></span>555-014-2207</li>
    <li><span class="icon"><svg width="14" height="14" viewBox="0 0 24 24" fill="#fff"><rect x="6" y="2" width="12" height="6"/><rect x="2" y="9" width="20" height="9" rx="1"/><rect x="6" y="15" width="12" height="7" fill="#fff" stroke="var(--teal)" stroke-width="1.5"/></svg></span>555-014-8830</li>
    <li><span class="icon"><svg width="14" height="14" viewBox="0 0 16 16" fill="none" stroke="#fff" stroke-width="1.3"><circle cx="8" cy="8" r="6.5"/><ellipse cx="8" cy="8" rx="3" ry="6.5"/><line x1="1.5" y1="8" x2="14.5" y2="8"/></svg></span><span>Dana@HarborlineRMS.com<br>www.HarborlineRMS.com</span></li>
  </ul>
</section>

</body>
</html>
```